Flyer für Immobilienfirma
Zielgruppe
Immobilienfirma, klassisches Maklerunternehmen, Zielgruppe in erster Linie Familien.
Aufgabenstellung
Wir benötigen eine klassische Weihnachtskarte für unsere Kunden. Sehr schön wäre es, wenn unser Logo (als Datei anbei) mit auf der Karte erscheint. Es ist eine kreative, moderne, graphische Umsetzung des Themas 'Frohe Weihnachten' erwünscht, bitte eine Fotolösungen mit Weihnachtsbildern. Die Rückseite sollte inhaltlich wie im Beispiel gestaltet sein, die Schrift bitte aber passend zum Design der Vorderseite wählen. Wichtig, da die Karte am Ende über die Druckerei adresstechnisch personalisiert wird, benötigen wir am Ende noch die Schriftart.

```html
<!DOCTYPE html>
<html lang="de">
<head>
<meta charset="utf-8">
<title>Weihnachtskarte Hallmeier Immobilien</title>
<link rel="stylesheet" href="https://fonts.googleapis.com/css2?family=Great+Vibes&family=Roboto:ital,wght@0,400;0,700;0,900;1,400&display=swap">
<style>
  :root {
    --stage: #f1f1f1;
    --red-light: #c0303a;
    --red: #b8222c;
    --red-dark: #a51c28;
    --white: #ffffff;
    --ink: #2b2b2b;
    --rule: #9a9a9a;
    --gold: #c9a95a;
  }
  * { box-sizing: border-box; margin: 0; padding: 0; }
  html, body { width: 1200px; height: 800px; overflow: hidden; }
  body {
    background: var(--stage);
    font-family: "Roboto", Arial, sans-serif;
    position: relative;
  }
  .card {
    position: absolute;
    left: 240px;
    width: 720px;
    height: 340px;
    overflow: hidden;
    box-shadow: 0 14px 28px rgba(0,0,0,.18);
  }
  .card--front {
    top: 35px;
    background: linear-gradient(135deg, var(--red-light), var(--red) 55%, var(--red-dark));
  }
  .card--back {
    top: 420px;
    display: flex;
    background: var(--white);
  }

  /* Front */
  .greeting {
    position: absolute;
    left: 62px;
    top: 110px;
    color: var(--white);
  }
  .greeting__script {
    font-family: "Great Vibes", cursive;
    font-size: 52px;
    line-height: 1;
    font-weight: 400;
    white-space: nowrap;
  }
  .greeting__bold {
    font-weight: 900;
    font-size: 32px;
    line-height: 1.15;
    letter-spacing: .5px;
    margin-left: 60px;
    margin-top: -4px;
    text-transform: uppercase;
  }
  .ornament-tree {
    position: absolute;
    right: -14px;
    top: -30px;
    width: 320px;
    height: 390px;
    clip-path: polygon(50% 0, 100% 100%, 0 100%);
    background:
      radial-gradient(circle at 50% 55%, rgba(255,255,255,.95), rgba(255,255,255,.78) 45%, rgba(246,214,217,.7) 100%);
  }
  .brand-disc {
    position: absolute;
    right: 91px;
    top: 110px;
    width: 110px;
    height: 110px;
    border-radius: 50%;
    background: var(--white);
    border: 3px solid var(--red);
    display: flex;
    align-items: center;
    justify-content: center;
  }
  .brand-name {
    font-family: "Roboto", Arial, sans-serif;
    font-weight: 700;
    font-size: 17px;
    color: var(--red);
  }

  /* Back */
  .message-side {
    position: relative;
    width: 62%;
    height: 100%;
    background: linear-gradient(135deg, var(--red), var(--red-dark));
    color: var(--white);
    padding: 34px 30px 20px 40px;
  }
  .salutation {
    font-style: italic;
    font-weight: 400;
    font-size: 14px;
    line-height: 1.3;
    margin-bottom: 10px;
  }
  .message p {
    font-size: 9.5px;
    line-height: 1.45;
    margin-bottom: 7px;
    max-width: 320px;
  }
  .sender {
    display: flex;
    gap: 40px;
    margin-top: 14px;
    font-size: 10px;
    line-height: 1.5;
  }
  .sender address { font-style: normal; }
  .contact li {
    list-style: none;
    display: flex;
    align-items: center;
    gap: 6px;
  }
  .contact svg { width: 11px; height: 11px; }
  .award-badge {
    position: absolute;
    right: 36px;
    top: 24px;
    width: 46px;
    height: 88px;
    background: linear-gradient(180deg, #d9bf7b, var(--gold));
    border: 2px solid var(--white);
    clip-path: polygon(0 0, 100% 0, 100% 88%, 50% 100%, 0 88%);
  }
  .back-brand {
    position: absolute;
    right: 26px;
    bottom: 60px;
    display: flex;
    align-items: center;
    gap: 6px;
  }
  .back-brand .brand-name { color: var(--white); font-size: 16px; }
  .back-brand__dot {
    width: 12px; height: 12px; border-radius: 50%; background: var(--white);
  }
  .address-side {
    position: relative;
    flex: 1;
    padding: 28px 26px;
  }
  .postage-frame {
    position: absolute;
    right: 26px;
    top: 24px;
    width: 90px;
    height: 50px;
    border: 1.5px solid var(--ink);
  }
  .address-lines {
    position: absolute;
    left: 26px;
    right: 26px;
    top: 150px;
  }
  .address-lines span {
    display: block;
    height: 32px;
    border-bottom: 1px solid var(--rule);
  }
</style>
</head>
<body>

<section class="card card--front">
  <div class="greeting">
    <h1 class="greeting__script">Frohe Weihnachten</h1>
    <p class="greeting__bold">Und ein gutes<br>neues Jahr</p>
  </div>
  <div class="ornament-tree" role="img" aria-label="Tannenbaum aus weißen und roten Weihnachtssymbolen: Kränze, Geschenke, Rentiere, Mützen, Schleifen, Fäustlinge, Strumpf, Schneeflocken und Schneemann"></div>
  <div class="brand-disc"><span class="brand-name">Hallmeier</span></div>
</section>

<section class="card card--back">
  <div class="message-side">
    <h2 class="salutation">Liebe Kunde,<br>Geschäftspartner und Freunde!</h2>
    <div class="message">
      <p>Wir möchten uns für Ihr entgegengebrachtes Vertrauen und die angenehme Zusammenarbeit bedanken.</p>
      <p>Genießen Sie die Weihnachtszeit mit vielen kleinen Freuden und kommen Sie gesund ins Jahr 2025.</p>
      <p>Aufgrund der aktuellen Notlage vieler Menschen möchten wir in diesem Jahr erneut mit einer Spende an den Kinderfonds der Stadt Auenfeld versuchen, ein wenig Freude und Zuversicht zu schenken.</p>
    </div>
    <div class="sender">
      <address>
        Ihr Immobilienteam von<br>Hallmeier Immobilien<br>Brunnengasse 7<br>90000 Auenfeld
      </address>
      <ul class="contact">
        <li><svg viewBox="0 0 12 12" aria-hidden="true"><rect x="1" y="2.5" width="10" height="7" fill="none" stroke="#fff"/><path d="M1 2.5l5 4 5-4" fill="none" stroke="#fff"/></svg>09876 543210</li>
        <li><svg viewBox="0 0 12 12" aria-hidden="true"><circle cx="6" cy="6" r="5" fill="none" stroke="#fff"/><path d="M1 6h10M6 1c-3 3-3 7 0 10M6 1c3 3 3 7 0 10" fill="none" stroke="#fff"/></svg>www.hallmeier-immobilien.de</li>
      </ul>
    </div>
    <div class="award-badge"></div>
    <div class="back-brand"><span class="back-brand__dot"></span><span class="brand-name">Hallmeier</span></div>
  </div>
  <div class="address-side">
    <div class="postage-frame"></div>
    <div class="address-lines"><span></span><span></span><span></span><span></span></div>
  </div>
</section>

</body>
</html>
```